Etiketten-Design für nachhaltige Vermarktung von Honig- und Bienenprodukten
Zielgruppe
Wir sind ein junges Unternehmen, welches sich auf die nachhaltige Vermarktung von Honig- und Bienenprodukten spezialisiert. Unsere Zielgruppe sind ernährungsbewusste Menschen im jungen und mittleren Alter, welche ein modernes Design mit Wiedererkennungswert anspricht. Wir suchen für unsere Honigproduktion ein dementsprechend geeignetes Etikettendesign.
Aufgabenstellung
Du hattest einen harten Arbeitstag. Das Letzte worauf du jetzt noch Lust hast, ist in einen Supermarkt zu gehen. Leider lässt sich dies nicht vermeiden, denn dir fehlen noch wesentliche Utensilien für den täglichen Bedarf. Du nimmst eine Abkürzung quer durch die Abteilung für Süß-Aufstriche und....WOOOOW..., was ist das denn für ein verrücktes Zeugs??? Ohne es zu wollen, musst du es kaufen ;-)
Folgende Vorgaben müssen berücksichtigt werden:
Das Produktlabel lautet: SUMM MIR ZU?! (auffallend)
Wir starten zu Beginn mit 3 Sorten: Robinie, Raps, Wald (auffallend)
Firmenlogo (auffallend; SUMM MIR ZU?! jedoch als Eyecatcher)
Deutscher Honig (dezent)
Füllmenge (Schriftgröße mindestens 4mm): 250g (dezent)
Name, Anschrift und Rufnummer (dezent)
Mindesthaltbarkeitsdatum (MHD): TT.MM.JJJJ (dezent)
Loskennzeichnung: XXX (dezent)
Liebevoll hergestellt nach den Qualitätsstandards des Norddeutschen Wachsvereins (N.W.V. e.V.) (dezent)
Trocken und vor Wärme geschützt lagern! (dezent)
Für Kinder unter 12 Monaten nicht geeignet (dezent)
Ein Gewährverschluss mit bedrucktem Deckeletikett soll ebenfalls vorhanden sein
Die exakten Maße des Etiketts sind derzeit nicht bekannt und deshalb flexibel.
Wichtig ist für uns, dass wir die Dateien zukünftig selbstständig bearbeiten können, wenn wir z.B. das Mindesthaltbarkeitsdatum und Chargennummer ändern möchten, sowie eine neue neue Sorte einführen.
In den beigefügten Dateien befindet sich unser Firmenlogo und einige Design-Beispiele, welche uns gefallen. Ebenfalls sind Bilder von möglichen Gläsern und Deckeln inkl. Maße vorhanden.
Bei Fragen gerne melden.

```html
<!DOCTYPE html>
<html lang="de">
<head>
<meta charset="utf-8">
<title>SUMM MIR ZU?! – Honigetikett Wald</title>
<link rel="stylesheet" href="https://fonts.googleapis.com/css2?family=Caveat+Brush&family=Comfortaa:wght@500;700&family=Montserrat:wght@600&display=swap">
<style>
  :root {
    --paper: #ffffff;
    --ink: #111111;
    --seal-black: #050505;
    --honey-light: #f6b433;
    --honey-mid: #ec9a2e;
    --honey-deep: #cf6a28;
    --brand-orange: #f6a623;
    --forest-green: #6cbf3c;
    --label-text: #1a1209;
    --white: #ffffff;
    --illustration-tone: #e8a23a;
  }
  * { box-sizing: border-box; margin: 0; padding: 0; }
  html, body {
    width: 1200px;
    height: 854px;
    overflow: hidden;
    background: var(--paper);
  }
  .artboard {
    position: relative;
    width: 1200px;
    height: 854px;
  }

  /* Lid seal label */
  .seal-label {
    position: absolute;
    left: 245px;
    top: 50px;
    width: 170px;
  }
  .seal-label__disc {
    width: 170px;
    height: 170px;
    border-radius: 50%;
    background: var(--seal-black);
    display: flex;
    align-items: center;
    justify-content: center;
  }
  .seal-label__strip {
    width: 74px;
    height: 210px;
    margin: -14px auto 0;
    background: var(--seal-black);
    display: flex;
    align-items: center;
    justify-content: center;
  }
  .brand-name {
    font-family: "Montserrat", sans-serif;
    font-weight: 600;
    color: var(--brand-orange);
    letter-spacing: 0.18em;
  }
  .brand-name--disc { font-size: 22px; }
  .brand-name--strip {
    font-size: 26px;
    writing-mode: vertical-rl;
  }

  /* Wrap-around label */
  .jar-label {
    position: absolute;
    left: 60px;
    top: 420px;
    width: 1080px;
    height: 330px;
    display: flex;
    background: linear-gradient(90deg,
      var(--honey-deep) 0%, var(--honey-mid) 8%, var(--honey-light) 16%,
      var(--honey-mid) 24%, var(--honey-deep) 32%, var(--honey-mid) 40%,
      var(--honey-light) 50%, var(--honey-mid) 60%, var(--honey-light) 68%,
      var(--honey-mid) 78%, var(--honey-deep) 90%, var(--honey-mid) 100%);
  }
  .label-panel {
    position: relative;
    width: 540px;
    height: 330px;
  }

  .illustration {
    position: absolute;
    border-radius: 40px;
    background: radial-gradient(ellipse at center, var(--illustration-tone) 0%, rgba(232,162,58,0) 75%);
  }
  .front .illustration { left: 60px; top: 20px; width: 420px; height: 150px; }
  .back .illustration { left: 20px; top: 40px; width: 240px; height: 210px; }

  .product-title {
    position: absolute;
    left: 0;
    width: 540px;
    top: 160px;
    text-align: center;
    font-family: "Caveat Brush", cursive;
    font-size: 78px;
    line-height: 1;
    color: var(--white);
    text-shadow: 2px 2px 0 var(--ink);
    transform: rotate(-3deg);
  }
  .variety {
    position: absolute;
    left: 185px;
    top: 262px;
    width: 170px;
    height: 42px;
    background: var(--forest-green);
    border-radius: 6px 14px 8px 12px;
    font-family: "Comfortaa", sans-serif;
    font-weight: 700;
    font-size: 30px;
    line-height: 42px;
    text-align: center;
    color: var(--label-text);
  }

  .legal {
    position: absolute;
    right: 60px;
    top: 28px;
    width: 300px;
    text-align: right;
    font-family: "Comfortaa", sans-serif;
    font-weight: 500;
    color: var(--label-text);
  }
  .legal__origin { font-size: 9.5px; line-height: 1.45; }
  .legal__address { font-size: 9.5px; line-height: 1.5; margin-top: 14px; }
  .legal__batch {
    margin-top: 14px;
    display: flex;
    justify-content: flex-end;
    align-items: center;
    gap: 6px;
    font-size: 12px;
    line-height: 1.45;
  }
  .batch-field {
    width: 96px;
    height: 34px;
    background: var(--white);
  }
  .legal__notes { font-size: 12px; line-height: 1.2; margin-top: 10px; }
  .legal__weight {
    margin-top: 14px;
    font-size: 13px;
  }
  .legal__weight strong {
    font-size: 30px;
    font-weight: 500;
    margin-left: 4px;
  }
</style>
</head>
<body>
<main class="artboard">

  <section class="seal-label" aria-label="Deckeletikett">
    <div class="seal-label__disc"><span class="brand-name brand-name--disc">VELLORA</span></div>
    <div class="seal-label__strip"><span class="brand-name brand-name--strip">VELLORA</span></div>
  </section>

  <section class="jar-label" aria-label="Glasetikett">
    <div class="label-panel front">
      <div class="illustration" role="img" aria-label="Illustration: zwei verliebte Cartoon-Bienen mit Herz"></div>
      <h1 class="product-title">SUMM MIR ZU?!</h1>
      <p class="variety">Wald</p>
    </div>

    <div class="label-panel back">
      <div class="illustration" role="img" aria-label="Illustration: fliegende Cartoon-Biene mit Herz"></div>
      <div class="legal">
        <p class="legal__origin">Deutscher Honig<br>Liebevoll hergestellt nach den<br>Qualitätsstandards des Norddeutschen<br>Wachsvereins (N.W.V. e.V.)</p>
        <p class="legal__address">SUMM MIR ZU?!<br>Jonas Lindqvist<br>Heideweg 12<br>24568 Kleinhorst<br>0431 998 207</p>
        <div class="legal__batch">
          <p>Mind. haltbar bis:<br>Los Nr:</p>
          <span class="batch-field"></span>
        </div>
        <p class="legal__notes">Trocken und vor Wärme geschützt lagern!<br>Für Kinder unter 12 Monaten nicht geeignet.</p>
        <p class="legal__weight">Füllmenge: <strong>250g</strong></p>
      </div>
    </div>
  </section>

</main>
</body>
</html>
```